Letterhead and compliment slip

We are a UK-based market research agency. We are looking for a new letterhead design to incorporate our logo, address details and company information. We are looking for a simple design. It should be modern. It needs to have a qualify feel. As we are UK based it needs to be designed for A4 paper size (letterhead).
I'm really looking for something simple in design terms!
Both letterhead and compliment slip need to include:
Our logo
Company address
Telephone number
Email address
Website address
Company registration number
VAT registration number
Grey and green would be a good colour scheme to fit with our logo

```html
<!DOCTYPE html>
<html lang="en">
<head>
<meta charset="utf-8">
<title>Insightwell Research – Letterhead and Compliment Slip</title>
<link href="https://fonts.googleapis.com/css2?family=Questrial&family=Roboto:wght@400&family=Pinyon+Script&display=swap" rel="stylesheet">
<style>
  :root {
    --bg: #dcdcdc;
    --paper: #f6f6f6;
    --green: #a6c93a;
    --grey-bar: #a7a8aa;
    --ink: #4a4a4a;
    --ink-soft: #5c5c5c;
    --rule: #c9c9c9;
  }
  * { margin: 0; padding: 0; box-sizing: border-box; }
  html, body { width: 1200px; height: 1022px; overflow: hidden; }
  body { background: var(--bg); position: relative; font-family: "Questrial", sans-serif; color: var(--ink); }

  .sheet { position: absolute; background: var(--paper); }
  .edge { position: absolute; left: 0; top: 0; bottom: 0; width: 8px; background: var(--green); }
  .edge::before { content: ""; position: absolute; left: 0; top: 0; width: 8px; height: 72px; background: var(--grey-bar); }

  .brand { position: absolute; display: flex; align-items: center; gap: 8px; }
  .brand-dot { width: 22px; height: 22px; border-radius: 50%; background: var(--green); }
  .brand-name { font-family: "Questrial", sans-serif; font-size: 30px; color: var(--green); letter-spacing: -0.3px; }

  .contact { position: absolute; padding-left: 13px; border-left: 1px solid var(--rule);
             font-family: "Roboto", sans-serif; font-size: 9.5px; line-height: 12px; color: var(--ink-soft); }
  .contact .company { color: var(--green); }
  .contact .lines { margin-bottom: 4px; }
  .contact .row { display: flex; align-items: center; gap: 5px; }
  .contact svg { width: 9px; height: 9px; fill: var(--green); flex: none; }

  /* letterhead */
  .letterhead { left: 80px; top: 75px; width: 614px; height: 865px; }
  .letterhead .brand { left: 45px; top: 74px; }
  .letterhead .contact { left: 397px; top: 48px; }
  .salutation { position: absolute; left: 53px; top: 242px; font-size: 16px; }
  .letter-body { position: absolute; left: 53px; top: 289px; width: 511px; font-size: 9.4px; line-height: 13px; }
  .letter-body p { margin-bottom: 13px; }
  .sign-off { position: absolute; left: 53px; top: 567px; font-size: 9.4px; }
  .legal-footer { position: absolute; left: 108px; top: 812px; font-family: "Roboto", sans-serif; font-size: 9.5px; color: var(--ink-soft); }
  .legal-footer .sep { margin: 0 11px; }

  /* compliment slip */
  .slip { left: 511px; top: 492px; width: 620px; height: 281px; }
  .slip .brand { left: 32px; top: 52px; }
  .slip .contact { left: 420px; top: 34px; }
  .slip-rule { position: absolute; left: 32px; top: 234px; width: 572px; height: 1px; background: var(--rule); }
  .slip-legal { position: absolute; left: 32px; font-family: "Roboto", sans-serif; font-size: 9.5px; color: var(--ink-soft); }
  .slip-legal.vat { top: 220px; }
  .slip-legal.reg { top: 237px; }
  .greeting { position: absolute; left: 309px; top: 188px; font-family: "Pinyon Script", cursive; font-size: 46px; color: var(--green); line-height: 1; }
</style>
</head>
<body>

<svg width="0" height="0" style="position:absolute">
  <symbol id="icon-phone" viewBox="0 0 24 24"><path d="M6.6 10.8a15.1 15.1 0 0 0 6.6 6.6l2.2-2.2c.3-.3.7-.4 1-.2 1.1.4 2.3.6 3.6.6.6 0 1 .4 1 1V20c0 .6-.4 1-1 1C10.6 21 3 13.4 3 4c0-.6.4-1 1-1h3.5c.6 0 1 .4 1 1 0 1.3.2 2.5.6 3.6.1.3 0 .7-.2 1z"/></symbol>
  <symbol id="icon-mail" viewBox="0 0 24 24"><path d="M2 5h20v14H2z M2 5l10 8 10-8" /></symbol>
  <symbol id="icon-web" viewBox="0 0 24 24"><circle cx="12" cy="12" r="10"/></symbol>
</svg>

<section class="sheet letterhead">
  <div class="edge"></div>
  <div class="brand"><span class="brand-dot"></span><span class="brand-name">Insightwell</span></div>
  <address class="contact" style="font-style:normal">
    <div class="company">Insightwell Research Ltd.</div>
    <div class="lines">12 Linden Court, Mill Lane<br>Harpenden<br>Hertfordshire, AL5 2QT</div>
    <div class="row"><svg><use href="#icon-phone"/></svg>+44 (0)1632 960418</div>
    <div class="row"><svg><use href="#icon-mail"/></svg>hello@insightwellresearch.co.uk</div>
    <div class="row"><svg><use href="#icon-web"/></svg>www.insightwellresearch.co.uk</div>
  </address>

  <p class="salutation">Dear Mr. Harlow,</p>
  <div class="letter-body">
    <p>Lorem ipsum dolor sit amet, consectetur adipiscing elit. Donec orci purus, luctus vitae dignissim eu, iaculis sed purus. Vivamus faucibus, ipsum nec aliquet viverra, leo mauris condimentum ligula, sit amet sagittis enim ligula quis arcu. Nam egestas tortor id nisi porttitor mattis. In tortor ante, ultricies in suscipit a, tempus non massa. Vivamus et auctor mi. Fusce vel massa nulla. Phasellus nec eros mauris, et scelerisque orci.</p>
    <p>Donec malesuada orci vitae nulla accumsan porta a id massa. Quisque accumsan iaculis magna sit amet fringilla. Maecenas consequat, magna eget tincidunt semper, odio nibh rutrum mi, id feugiat ante nisi eu risus. Vestibulum nunc orci, rhoncus a placerat in, ultricies in mi. Cras mattis varius eros, vel fringilla nisi suscipit eget. Quisque scelerisque sagittis nulla at porttitor.</p>
    <p>Sed id augue vitae urna euismod commodo aliquet a quam. Pellentesque arcu velit, consequat et diam. Nullam erat sem, rhoncus id ullamcorper vitae, rhoncus et arcu. In ut nisi iaculis at. Donec eu magna a metus ornare faucibus. Fusce aliquet faucibus ultricies, idunt gravida, sem arcu adipiscing lacus, ac bibendum nulla leo eu purus. Quisque nec accumsan quis quis nibh. Vestibulum id purus lorem.</p>
    <p>It is a long established fact that a reader will be distracted by the readable content of a page when looking at its layout. The point of using Lorem Ipsum is that it has a more-or-less normal distribution of letters, as opposed to using 'Content here, content here', making it look like readable English. Many desktop publishing packages.</p>
  </div>
  <p class="sign-off">Sincerely,</p>
  <p class="legal-footer">Company registration number : 6041127<span class="sep">|</span>VAT registration number: : 731254906</p>
</section>

<section class="sheet slip">
  <div class="edge"></div>
  <div class="brand"><span class="brand-dot"></span><span class="brand-name">Insightwell</span></div>
  <address class="contact" style="font-style:normal">
    <div class="company">Insightwell Research Ltd</div>
    <div class="lines">12 Linden Court, Mill Lane<br>Harpenden<br>Hertfordshire, AL5 2QT</div>
    <div class="row"><svg><use href="#icon-phone"/></svg>+44 (0)1632 960418</div>
    <div class="row"><svg><use href="#icon-mail"/></svg>hello@insightwellresearch.co.uk</div>
    <div class="row"><svg><use href="#icon-web"/></svg>www.insightwellresearch.co.uk</div>
  </address>
  <p class="greeting">With Compliments</p>
  <p class="slip-legal vat">VAT registration number: : 731254906</p>
  <div class="slip-rule"></div>
  <p class="slip-legal reg">Company registration number : 6041127</p>
</section>

</body>
</html>
```